Tot Haven child care center

We have a logo. Need help putting all info together in a brochure to attract clients and promote information.

Needed to include hours, address, phone number, webpage FB info and pictures of kids in a childcare setting.

Address and phone #
Maple Gate Shopping Center
482 W Orrin Fell Rd. Suite 214
Centerville, OH 45459
937-555-0148

Webpage: www.tothavenplace.example

FB: www.social.example/tothaven.place

Hours
Monday - Thursday
*6:30am - 10pm

Friday
*6:30am to 12am (midnight)

Saturday
9am to 12am (midnight)

Sunday
10am to 9pm

Child care center that offers drop-in and full time flexible child care. Open 7 days a week.

Other info to add:
We offer child care services to children 6 weeks to 12 years old. No reservations are required, Infants under 18 months require a reservation. We offer a Healthy Breakfast, Lunch, Dinner, and Snack Menu! If you have special dietary needs you can let us know and we will make accommodations

Ohio's first state-licensed drop-in, hourly childcare provider, Tot Haven provides you with top-rate, dependable childcare on the spur of the moment and your child with first-rate fun.
Experienced, friendly staff
CPR/first aid-certified staff
FBI/fingerprint background checks on all staff
Fire safety and secure environment
Breakfast/lunch/dinner menu
Snack menu
Art activities
Music time
Separate infant room
Outdoor play area
Secure door lock system
Convenient payment options

```html
<!DOCTYPE html>
<html lang="en">
<head>
<meta charset="utf-8">
<title>Tot Haven – Child Care Flyer</title>
<link href="https://fonts.googleapis.com/css2?family=Arimo:wght@400;700&display=swap" rel="stylesheet">
<style>
  :root {
    --backdrop: #7d7b7c;
    --green: #02d802;
    --yellow: #fff200;
    --pink: #e6127a;
    --text-pink: #e8198b;
    --white: #ffffff;
    --sky-top: #52d0fa;
    --sky-bottom: #08b3f6;
  }
  * { box-sizing: border-box; margin: 0; padding: 0; }
  html, body { width: 1200px; height: 1000px; overflow: hidden; }
  body {
    background: var(--backdrop);
    font-family: "Arimo", Arial, sans-serif;
    color: var(--text-pink);
    position: relative;
  }
  .flyer {
    position: absolute;
    left: 224px; top: 13px;
    width: 753px; height: 975px;
    background: var(--white);
    box-shadow: 0 0 12px rgba(0,0,0,0.55);
    overflow: hidden;
  }
  .hours {
    position: absolute; left: 0; top: 0;
    width: 100%; height: 186px;
    background: var(--green);
  }
  .hours-title {
    position: absolute; left: 39px; top: 22px;
    font-size: 22px; font-weight: 400; letter-spacing: 0.3px;
  }
  .hours-table {
    position: absolute; left: 41px; top: 57px;
    border-collapse: collapse; font-size: 14.5px;
  }
  .hours-table td { height: 22px; padding: 0; vertical-align: middle; white-space: nowrap; }
  .hours-table .day { width: 187px; }
  .hours-table .sep { width: 29px; }
  .hours-note {
    position: absolute; left: 38px; top: 155px; font-size: 14.5px; white-space: nowrap;
  }
  .band { position: absolute; left: 0; width: 100%; }
  .band-yellow-top { top: 186px; height: 13px; background: var(--yellow); }
  .band-pink-top { top: 199px; height: 11px; background: var(--pink); }
  .band-pink-bottom { top: 555px; height: 12px; background: var(--pink); }
  .band-yellow-bottom { top: 567px; height: 14px; background: var(--yellow); }
  .brand {
    position: absolute; left: 0; top: 254px; width: 100%;
    display: flex; justify-content: center; align-items: center; gap: 8px;
  }
  .brand-dot { width: 14px; height: 14px; border-radius: 50%; background: var(--pink); }
  .brand-name { font-size: 30px; font-weight: 700; color: var(--pink); }
  .contact {
    position: absolute; top: 246px;
    font-size: 12.5px; line-height: 16px; white-space: nowrap;
  }
  .contact-address { left: 40px; }
  .contact-online { right: 24px; text-align: right; }
  .kids-photo {
    position: absolute; left: 0; top: 338px; width: 100%; height: 212px;
    background: linear-gradient(90deg, #f4836b 0%, #c97ab8 18%, #f04e9a 32%, #56b8ea 48%, #f5c62a 62%, #ec3f97 76%, #4f8ed0 92%, #ffffff 100%);
    opacity: 0.75;
  }
  .info {
    position: absolute; left: 0; top: 581px; width: 100%; height: 394px;
    background: linear-gradient(180deg, var(--sky-top) 0%, var(--sky-bottom) 100%);
  }
  .info p {
    position: absolute; left: 40px; width: 690px;
    font-size: 14.8px; line-height: 17.6px;
  }
  .intro { top: 20px; }
  .info .licensed { top: 90px; left: 39px; }
  .features {
    position: absolute; left: 41px; top: 146px;
    list-style: none; font-size: 14.8px; line-height: 17.7px;
  }
  .snapshot {
    position: absolute; width: 128px; height: 128px; border-radius: 50%;
    border: 4px solid var(--yellow);
    box-shadow: 0 0 10px 3px rgba(255,255,190,0.9);
  }
  .snapshot-infant { left: 285px; top: 222px; background: radial-gradient(circle, #f3c3a8 0%, #e86a8e 55%, #7cc46a 100%); }
  .snapshot-toddler { left: 440px; top: 224px; background: radial-gradient(circle, #e8b895 0%, #4f88c2 55%, #7a6a55 100%); }
  .snapshot-baby { left: 596px; top: 226px; background: radial-gradient(circle, #b07a5a 0%, #c49ad8 55%, #f7f7f7 100%); }
</style>
</head>
<body>
<main class="flyer">
  <section class="hours">
    <h1 class="hours-title">OPEN HOURS</h1>
    <table class="hours-table">
      <tr><td class="day">MONDAY&nbsp; - THURSDAY</td><td class="sep">:</td><td>6:30 AM - 10 PM</td></tr>
      <tr><td class="day">FRIDAY</td><td class="sep">:</td><td>6:30 AM - 12 AM (MIDNIGHT)</td></tr>
      <tr><td class="day">SATURDAY</td><td class="sep">:</td><td>9 AM - 12 AM (MIDNIGHT)</td></tr>
      <tr><td class="day">SUNDAY</td><td class="sep">:</td><td>10 AM - &nbsp;9 PM</td></tr>
    </table>
    <p class="hours-note">Child care center that offers drop-in and full time flexible child care. Open 7 days a week.</p>
  </section>

  <div class="band band-yellow-top"></div>
  <div class="band band-pink-top"></div>

  <address class="contact contact-address" style="font-style:normal">
    Maple Gate Shopping Center<br>
    482 W Orrin Fell Rd. Suite 214<br>
    Centerville, OH 45459
  </address>

  <div class="brand">
    <span class="brand-dot"></span>
    <span class="brand-name">Tot Haven</span>
  </div>

  <div class="contact contact-online">
    937-555-0148<br>
    www.tothavenplace.example<br>
    www.social.example/tothaven.place
  </div>

  <div class="kids-photo" role="img" aria-label="Seven smiling children in colourful clothes lying in a row on a white background"></div>

  <div class="band band-pink-bottom"></div>
  <div class="band band-yellow-bottom"></div>

  <section class="info">
    <p class="intro">We offer child care services to children 6 weeks to 12 years old. No reservations are required, Infants under 18 months require a reservation. We offer a Healthy Breakfast, Lunch, Dinner, and Snack Menu! If you have special dietary needs you can let us know and we will make accommodations</p>
    <p class="licensed">Ohio's first state-licensed drop-in, hourly childcare provider, Tot Haven provides you with top-rate, dependable childcare on the spur of the moment and your child with first-rate fun.</p>
    <ul class="features">
      <li>Experienced, friendly staff</li>
      <li>CPR/first aid-certified staff</li>
      <li>FBI/fingerprint background checks on all staff</li>
      <li>Fire safety and secure environment</li>
      <li>Breakfast/lunch/dinner menu</li>
      <li>Snack menu</li>
      <li>Art activities</li>
      <li>Music time</li>
      <li>Separate infant room</li>
      <li>Outdoor play area</li>
      <li>Secure door lock system</li>
      <li>Convenient payment options</li>
    </ul>
    <div class="snapshot snapshot-infant" role="img" aria-label="Infant in a pink outfit playing with toys"></div>
    <div class="snapshot snapshot-toddler" role="img" aria-label="Young boy playing with toy cars at a table"></div>
    <div class="snapshot snapshot-baby" role="img" aria-label="Smiling baby in a lilac top"></div>
  </section>
</main>
</body>
</html>
```